Driver License Monitoring Application Marketing Website

We need a new web design for our web application. The product is called "PermitSentry." We provide a driver license monitoring service to companies and local government bodies with driver fleets. Our current website is available at www.PermitSentry-demo.net.

I prefer a clean, single-page design with good SEO. Attached are some PDFs with data about the project.

Target Market(s)

Companies with driver fleets, local government.

Industry/Entity Type

Government

Coding

Coded - Design and coding required

Number of Pages Required

1 page

Colors
000000

Requirements
Must have
• Content from current www.PermitSentry-demo.net and attached PDFs.
Nice to have
• Prefer a simple Bootstrap or similar design for easy editing.
• Room for a simple video explanation of how the product works (we don't have an actual video yet)

```html
<!DOCTYPE html>
<html lang="en">
<head>
<meta charset="utf-8">
<title>PermitSentry – Driver License Monitoring</title>
<link rel="stylesheet" href="https://fonts.googleapis.com/css2?family=Cinzel:wght@400;700&family=Lato:wght@400;700&display=swap">
<style>
:root{
  --red:#b31b20;
  --black:#000;
  --ink:#1a1a1a;
  --text:#333;
  --muted:#8a8a8a;
  --rule:#e2e2e2;
  --hero-a:#d6d6d6;
  --hero-b:#f1f1f1;
  --band:#1b1b1b;
  --footer:#1f1f1f;
  --footer-base:#262626;
  --white:#fff;
}
*{box-sizing:border-box;margin:0;padding:0}
html,body{width:838px;height:1200px;overflow:hidden;background:var(--white)}
body{position:relative;font-family:"Lato",Arial,sans-serif;color:var(--text)}
ul{list-style:none}

/* header */
.site-header{position:absolute;left:0;top:0;width:838px;height:78px;background:var(--white)}
.brand{position:absolute;left:92px;top:29px;font-family:"Cinzel",Georgia,serif;font-weight:700;font-size:20px;color:var(--black);letter-spacing:.3px}
.main-nav{position:absolute;right:207px;top:37px;display:flex;gap:13px;font-size:9.6px;text-transform:uppercase;color:var(--ink);white-space:nowrap}
.main-nav .active{color:var(--red)}
.login-btn{position:absolute;left:643px;top:28px;width:71px;height:25px;background:var(--black);color:var(--white);font-size:10px;display:flex;align-items:center;justify-content:center;gap:6px}
.search-btn{position:absolute;left:720px;top:28px;width:26px;height:25px;background:var(--black);display:flex;align-items:center;justify-content:center}

/* hero */
.hero{position:absolute;left:0;top:78px;width:838px;height:259px;background:radial-gradient(ellipse at 60% 40%,var(--hero-b),var(--hero-a))}
.hero-visual{position:absolute;left:145px;top:26px;width:264px;height:214px;border-radius:6px;background:linear-gradient(180deg,#3a3a3a,#d0d0d0)}
.hero-title{position:absolute;left:472px;top:74px;font-family:"Cinzel",Georgia,serif;font-size:29px;letter-spacing:1px;color:var(--black);white-space:nowrap}
.hero-title span{color:var(--red)}
.hero-text{position:absolute;left:470px;top:118px;width:242px;text-align:center;font-size:11px;line-height:15px;color:#222}
.read-more{position:absolute;left:547px;top:174px;width:86px;height:21px;background:var(--black);color:var(--white);font-family:"Cinzel",Georgia,serif;font-size:11px;display:flex;align-items:center;justify-content:center}
.slide-arrow{position:absolute;top:112px;width:22px;height:38px;background:var(--white);display:flex;align-items:center;justify-content:center;box-shadow:0 0 4px rgba(0,0,0,.15)}
.slide-arrow.prev{left:46px;border-radius:0 20px 20px 0}
.slide-arrow.next{left:768px;border-radius:20px 0 0 20px}

/* section headings */
.section-title{position:absolute;font-size:15.5px;font-weight:700;color:var(--black);text-transform:uppercase;white-space:nowrap}
.section-title span{color:var(--red)}
.section-rule{position:absolute;height:1px;background:var(--rule)}

/* features */
.feature-list{position:absolute;left:92px;top:400px;width:230px;height:110px;border-left:1px solid #d0d0d0}
.feature-list li{position:absolute;left:0;font-size:16.5px;color:var(--ink);padding-left:40px;white-space:nowrap}
.feature-list li::before{content:"";position:absolute;left:0;top:50%;width:24px;height:1px;background:#d0d0d0}
.feature-list li::after{content:"";position:absolute;left:22px;top:calc(50% - 2px);width:5px;height:5px;border-radius:50%;background:#c8c8c8}
.feature-list .on{color:var(--red)}

.video{position:absolute;left:492px;top:398px;width:254px;height:151px;background:linear-gradient(120deg,#c4d2dc,#e9eef1 55%,#b8c3cc)}
.video-play{position:absolute;left:110px;top:51px;width:33px;height:33px;border-radius:50%;background:var(--white);display:flex;align-items:center;justify-content:center}
.video-bar{position:absolute;left:0;bottom:0;width:254px;height:17px;background:var(--black);color:var(--white);font-size:7px;display:flex;align-items:center;padding:0 6px;gap:6px}
.video-track{flex:1;height:4px;border-radius:2px;background:#444;position:relative}
.video-track::before{content:"";position:absolute;left:14px;top:-1px;width:6px;height:6px;border-radius:50%;background:#3b8fd6}

/* service band */
.service-band{position:absolute;left:0;top:576px;width:838px;height:183px;background:radial-gradient(circle at 15% 60%,#3a3a3a,transparent 30%),radial-gradient(circle at 95% 40%,#333,transparent 25%),var(--band)}
.service{position:absolute;top:42px;width:160px;text-align:center;color:var(--white)}
.service-icon{width:68px;height:68px;margin:0 auto;border:2px solid var(--white);border-radius:50%;display:flex;align-items:center;justify-content:center}
.service-icon.accent{background:var(--red);border-width:3px}
.service h3{font-size:13px;font-weight:700;margin-top:12px}
.service p{font-size:10.5px;margin-top:3px;color:#ddd}

/* alerts & benefits */
.tick-list{position:absolute;font-size:10.2px;color:#222;white-space:nowrap}
.tick-list li{position:relative;height:16.8px;padding-left:18px;line-height:13px}
.tick-list li::before{content:"";position:absolute;left:4px;top:1px;width:4px;height:8px;border:solid var(--red);border-width:0 2.5px 2.5px 0;transform:rotate(40deg)}
.tick-list li.sub{padding-left:29px;height:14.9px}
.tick-list li.sub::before{display:none}
.truck-photo{position:absolute;left:310px;top:825px;width:196px;height:163px;border:2px solid var(--black);background:linear-gradient(180deg,#9fc3d9 0%,#8a4a52 50%,#555 100%)}

/* footer */
.site-footer{position:absolute;left:0;top:1017px;width:838px;height:115px;background:var(--footer);color:var(--white)}
.footer-brand{position:absolute;left:92px;top:24px;font-family:"Cinzel",Georgia,serif;font-weight:700;font-size:15px;color:var(--white)}
.footer-address{position:absolute;left:92px;top:51px;font-size:9.5px;line-height:16.5px;color:#8f8f8f;font-style:normal}
.footer-divider{position:absolute;top:23px;width:1px;height:66px;background:#3c3c3c}
.footer-heading{position:absolute;top:21px;font-size:12px;font-weight:400;text-transform:uppercase;color:var(--white)}
.newsletter-input{position:absolute;left:327px;top:55px;width:197px;height:29px;border:1px solid #3e3e3e;font-size:9.5px;color:#888;display:flex;align-items:center;justify-content:space-between;padding:0 10px}
.footer-contact{position:absolute;right:93px;top:43px;text-align:right;font-size:9.5px;line-height:16.6px;color:#8f8f8f}
.footer-contact b{color:var(--white);font-weight:700}
.footer-base{position:absolute;left:0;top:1132px;width:838px;height:68px;background:var(--footer-base)}
.social{position:absolute;left:375px;top:16px;display:flex;gap:7px}
.social span{width:17px;height:17px;border-radius:50%;background:#4a4a4a}
.copyright{position:absolute;left:0;top:44px;width:838px;text-align:center;font-size:9.5px;color:#8a8a8a}
</style>
</head>
<body>

<header class="site-header">
  <div class="brand">PermitSentry</div>
  <nav class="main-nav">
    <a class="active">Home</a><a>License-Monitoring</a><a>About Us</a><a>Contact Us</a>
  </nav>
  <div class="login-btn">
    <svg width="9" height="9" viewBox="0 0 10 10"><circle cx="5" cy="3" r="2.4" fill="#fff"/><path d="M0.5 10 C1 6 9 6 9.5 10Z" fill="#fff"/></svg>LOGIN
  </div>
  <div class="search-btn">
    <svg width="14" height="14" viewBox="0 0 14 14"><circle cx="5.5" cy="5.5" r="4.3" fill="none" stroke="#fff" stroke-width="1.6"/><path d="M8.7 8.7 13 13" stroke="#fff" stroke-width="2"/></svg>
  </div>
</header>

<section class="hero">
  <div class="slide-arrow prev"><svg width="8" height="10" viewBox="0 0 8 10"><path d="M7 0 1 5 7 10Z" fill="#111"/></svg></div>
  <div class="hero-visual" role="img" aria-label="Desktop monitor showing the fleet license summary dashboard"></div>
  <h1 class="hero-title">Online <span>Access</span></h1>
  <p class="hero-text">Review Your Fleet Status On Demand. Get Email Alerts When License Problems Arise. Track Your Drivers' Licenses Proactively.</p>
  <div class="read-more">READ MORE</div>
  <div class="slide-arrow next"><svg width="8" height="10" viewBox="0 0 8 10"><path d="M1 0 7 5 1 10Z" fill="#111"/></svg></div>
</section>

<h2 class="section-title" style="left:92px;top:360px">Monitor your <span>whole feet online</span></h2>
<div class="section-rule" style="left:92px;top:384px;width:368px"></div>
<ul class="feature-list">
  <li class="on" style="top:13px">Secure</li>
  <li style="top:44px">Available 24 hours a day</li>
  <li style="top:74px">Desktop or Mobie</li>
</ul>

<h2 class="section-title" style="left:494px;top:360px">Our <span>Video</span></h2>
<div class="section-rule" style="left:494px;top:384px;width:252px"></div>
<div class="video" role="img" aria-label="Product explainer video: businessman in an office with colleagues behind">
  <div class="video-play"><svg width="12" height="14" viewBox="0 0 12 14"><path d="M1 0 12 7 1 14Z" fill="#111"/></svg></div>
  <div class="video-bar">
    <svg width="7" height="8" viewBox="0 0 7 8"><path d="M0 0 7 4 0 8Z" fill="#fff"/></svg>
    <span>04:59</span><span class="video-track"></span><span>10:35</span>
    <svg width="9" height="8" viewBox="0 0 9 8"><path d="M0 2.5H2L5 0V8L2 5.5H0Z" fill="#fff"/><path d="M6.5 2Q8 4 6.5 6" stroke="#fff" fill="none"/></svg>
    <svg width="8" height="8" viewBox="0 0 8 8"><path d="M0 8 8 0M0 5V8H3M8 3V0H5" stroke="#fff" fill="none"/></svg>
  </div>
</div>

<section class="service-band">
  <div class="service" style="left:94px">
    <div class="service-icon accent">
      <svg width="26" height="32" viewBox="0 0 26 32"><path d="M13 1C6 1 2 6 2 11c0 5 4 7 5 11h12c1-4 5-6 5-11C24 6 20 1 13 1Z" fill="#fff"/><rect x="8" y="24" width="10" height="3" fill="#fff"/><rect x="9" y="28" width="8" height="3" fill="#fff"/></svg>
    </div>
    <h3>What We Do</h3><p>License Monitoring</p>
  </div>
  <div class="service" style="left:256px">
    <div class="service-icon">
      <svg width="32" height="32" viewBox="0 0 32 32" fill="#fff"><path d="M4 30V14l8-3v19Z"/><path d="M13 30V4l8 4v22Z"/><path d="M22 30V16h6v14Z"/></svg>
    </div>
    <h3>Commercial</h3><p>Private Sector</p>
  </div>
  <div class="service" style="left:418px">
    <div class="service-icon">
      <svg width="32" height="30" viewBox="0 0 32 30" fill="#fff"><path d="M16 1 2 8h28Z"/><rect x="3" y="9" width="26" height="3"/><rect x="5" y="13" width="3" height="11"/><rect x="11" y="13" width="3" height="11"/><rect x="18" y="13" width="3" height="11"/><rect x="24" y="13" width="3" height="11"/><rect x="2" y="25" width="28" height="4"/></svg>
    </div>
    <h3>Government</h3><p>Public Sector</p>
  </div>
  <div class="service" style="left:582px">
    <div class="service-icon">
      <svg width="34" height="28" viewBox="0 0 34 28" fill="#fff"><circle cx="13" cy="8" r="6.5"/><path d="M1 27c0-8 5-11 12-11s12 3 12 11Z"/><circle cx="24" cy="12" r="5" stroke="#1b1b1b" stroke-width="1.5"/><path d="M16 27c0-6 4-8 8-8s9 2 9 8Z" stroke="#1b1b1b" stroke-width="1.5"/></svg>
    </div>
    <h3>About Us</h3><p>Florida Law Authorities</p>
  </div>
</section>

<h2 class="section-title" style="left:91px;top:782px">Get instant <span>email alerts</span></h2>
<div class="section-rule" style="left:91px;top:805px;width:198px"></div>
<ul class="tick-list" style="left:93px;top:825px">
  <li>Suspensions For Child Support</li>
  <li>Suspensions For Unpaid Fines</li>
  <li>Suspensions For Court Obligations</li>
  <li>Revocations For Accidents</li>
  <li>Revocations For Convictions</li>
  <li>Commercial Vehicle Disqualifications</li>
  <li>Medical Certificate Expirations</li>
  <li>License Expirations</li>
  <li>License Cancellations</li>
  <li>All Other License Sanctions</li>
</ul>
<div class="truck-photo" role="img" aria-label="Red semi truck driving on a highway"></div>

<h2 class="section-title" style="left:535px;top:782px">Our <span>Benefits</span></h2>
<div class="section-rule" style="left:535px;top:805px;width:211px"></div>
<ul class="tick-list" style="left:534px;top:825px">
  <li>Recive license Alerts Immediately by Email</li>
  <li class="sub">- Suspensions</li>
  <li class="sub">- Revocations</li>
  <li class="sub">- Expirations</li>
  <li class="sub">- Cancellations</li>
  <li class="sub">- Disqualifications</li>
  <li class="sub">- Other Driver Sanctions</li>
  <li>Improve Public Safety</li>
  <li>Encourage Responsible Employee Behavior</li>
  <li>Reduce Insurance Premiums</li>
  <li>Increase Productivity</li>
</ul>

<footer class="site-footer">
  <div class="footer-brand">PermitSentry</div>
  <address class="footer-address">4410 Harbor Point Rd., Ste 118<br>Lakemont, FL 33999</address>
  <div class="footer-divider" style="left:287px"></div>
  <h4 class="footer-heading" style="left:349px">Sign up for newsletter</h4>
  <div class="newsletter-input"><span>Enter your email here</span><span style="color:#bbb">&rarr;</span></div>
  <div class="footer-divider" style="left:564px"></div>
  <h4 class="footer-heading" style="right:93px">Contact Us</h4>
  <div class="footer-contact">
    <b>M</b>: 1.555.201.4417<br>
    <b>F</b>: (555) 010-2290<br>
    <b>E</b>: contact@permitsentry-demo.net
  </div>
</footer>
<div class="footer-base">
  <div class="social"><span></span><span></span><span></span><span></span></div>
  <p class="copyright">© 2015 PermitSentry. All Rights Reserved.</p>
</div>

</body>
</html>
```